Flyer for American Indian Elders on Dementia Warning Signs

We need a flyer designed for older adults who are American Indian or Alaska Native (in the U.S.).

Ideally, the flyer should complement the colors of our logos. The project logo and our organization logo are attached to the brief.

When people see the flyer we want them to feel that it represents their culture, is warm, and professional but relatable to older adults and people who have limited incomes.

I have attached an earlier draft of the document we designed ourselves BUT we want different and better.

It is for older adults who have trouble reading so:
1. you must use a font that is 11.5 points or larger
2. Do not put text over complex pictures or use shading with words
3. You can use a serif font for the heading, but should use san serif for the body text
4. There should be good contrast between the font color and background

Please do not use any images that include a head dress or pictures of American Indian people or things that are very traditional or "token" imagery.

We need to save a small space under the call out box/ somewhere on the flyer for other people to add their logo once they download.

Let us know if you have questions or need additional information.

Target Market(s)

Older American Indian people

Font styles to use
Serif
Sans Serif

Requirements
Must have
• Easy to read for older adults
Should not have
• indian headdress

```html
<!DOCTYPE html>
<html lang="en">
<head>
<meta charset="utf-8">
<title>10 Warning Signs of Abnormal Memory Changes or Dementia</title>
<link rel="stylesheet" href="https://fonts.googleapis.com/css2?family=Crimson+Pro:wght@600&family=Arimo:wght@400;700&display=swap">
<style>
  :root {
    --teal: #4fa5ad;
    --teal-dark: #3f8f97;
    --clay: #b4584f;
    --ink: #2a2a2a;
    --white: #ffffff;
  }
  * { margin: 0; padding: 0; box-sizing: border-box; }
  html, body { width: 887px; height: 1200px; overflow: hidden; background: var(--white); }
  .flyer {
    position: relative; width: 887px; height: 1200px; overflow: hidden;
    font-family: "Arimo", "Helvetica Neue", Arial, sans-serif; color: var(--ink);
  }
  .hero { position: absolute; left: 0; top: 0; width: 887px; height: 338px; background: var(--teal); }
  .brand-tab {
    position: absolute; left: 343px; top: 0; width: 202px; height: 58px;
    background: var(--white); border-radius: 0 0 16px 16px;
    display: flex; align-items: center; justify-content: center; gap: 7px;
  }
  .brand-dot { width: 26px; height: 26px; border-radius: 50%; background: var(--teal); flex: none; }
  .brand-name { font-size: 11px; font-weight: 700; line-height: 1.15; color: var(--teal-dark); }
  .title {
    position: absolute; left: 0; top: 90px; width: 887px; text-align: center;
    font-family: "Crimson Pro", Georgia, serif; font-weight: 600;
    font-size: 41px; line-height: 43px; color: var(--white);
  }
  .intro {
    position: absolute; left: 104px; top: 192px; width: 679px; text-align: center;
    font-size: 15px; line-height: 20.5px; color: var(--white);
  }
  .intro p + p { margin-top: 14px; }
  .band {
    position: absolute; left: 0; width: 887px; height: 31px;
    background: linear-gradient(180deg, var(--teal) 0%, #8a7e79 50%, var(--clay) 100%);
  }
  .band--top { top: 337px; }
  .band--bottom { top: 983px; }
  .sign { position: absolute; font-size: 14px; line-height: 21.6px; }
  .sign strong { font-weight: 700; }
  .sign-icon {
    position: absolute; width: 44px; height: 44px; border-radius: 10px;
    background: linear-gradient(180deg, var(--teal) 0%, var(--clay) 100%);
  }
  .col-left .sign { left: 107px; width: 330px; }
  .col-right .sign { left: 519px; width: 320px; }
  .col-left .sign-icon { left: 49px; }
  .col-right .sign-icon { left: 463px; }
  .partner {
    position: absolute; left: 462px; top: 926px; height: 42px;
    display: flex; align-items: center; gap: 8px;
    border-left: 0;
  }
  .partner-square { width: 38px; height: 38px; background: var(--teal); flex: none; }
  .partner-name { font-size: 13px; font-weight: 700; line-height: 1.2; color: var(--clay); width: 170px; }
  .partner-mini {
    position: absolute; left: 716px; top: 928px; width: 56px;
    display: flex; flex-direction: column; align-items: center; gap: 3px;
  }
  .partner-mini .partner-square { width: 24px; height: 24px; }
  .partner-mini span { font-size: 5px; font-weight: 700; color: var(--clay); text-align: center; line-height: 1.1; }
  .footer { position: absolute; left: 0; top: 1014px; width: 887px; height: 186px; background: var(--clay); }
  .footer-text { position: absolute; left: 48px; top: 27px; width: 555px; font-size: 13px; line-height: 16.5px; color: var(--white); }
  .footer-text p + p { margin-top: 10px; }
  .callout {
    position: absolute; left: 630px; top: 17px; width: 239px; height: 153px;
    border-radius: 8px; overflow: hidden; background: var(--white);
  }
  .callout-head {
    height: 105px; background: var(--teal); color: var(--white);
    font-weight: 700; font-size: 17px; line-height: 24px; text-align: center;
    display: flex; align-items: center; justify-content: center; padding: 0 12px;
  }
  .callout-links { padding-top: 8px; text-align: center; font-size: 12.5px; line-height: 16.5px; color: var(--clay); }
</style>
</head>
<body>
<main class="flyer">
  <header class="hero">
    <div class="brand-tab">
      <span class="brand-dot"></span>
      <span class="brand-name">ELDER MIND<br>RESOURCE CENTER</span>
    </div>
    <h1 class="title">10 Warning Signs of Abnormal Memory<br>Changes or Dementia</h1>
    <div class="intro">
      <p>Everyone slows down as they get older. Most people see changes in their bodies and minds. Big changes that make it hard to get through the day are not a normal part of aging.</p>
      <p>Some people notice these changes in themselves. Sometimes, friends and family are the first to see changes in memory or how you act. If you have one or more of these 10 warning signs, see your doctor for help.</p>
    </div>
  </header>
  <div class="band band--top"></div>

  <section class="col-left">
    <div class="sign-icon" style="top:404px" role="img" aria-label="Head with question marks icon"></div>
    <p class="sign" style="top:398px"><strong>Memory loss that disrupts daily life:</strong> forgetting events or important dates, repeating yourself, or relying on things to help you remember more often like lists or sticky notes.</p>
    <div class="sign-icon" style="top:506px" role="img" aria-label="Checklist icon"></div>
    <p class="sign" style="top:500px"><strong>Harder to do familiar tasks at home, at work, or when you are out:</strong> having problems with driving places, using a cell phone, making a grocery list, or shopping.</p>
    <div class="sign-icon" style="top:610px" role="img" aria-label="Connected network icon"></div>
    <p class="sign" style="top:606px"><strong>Trouble with tasks that require your eyesight to connect with your thinking:</strong> having more problems with balance or telling distance, tripping over things at home, spilling or dropping things more often.</p>
    <div class="sign-icon" style="top:740px" role="img" aria-label="Thought cloud icon"></div>
    <p class="sign" style="top:735px"><strong>Losing things and not being able to retrace steps to find them:</strong> placing car keys in the washer or dryer or not being able to go back to find something you use everyday.</p>
    <div class="sign-icon" style="top:845px" role="img" aria-label="Two people apart icon"></div>
    <p class="sign" style="top:840px"><strong>Pulling away from work or time with friends and family:</strong> not wanting to go to church or cultural events, loss of interest in sex, not being able to follow radio shows or keep up with what's happening in sports games.</p>
  </section>

  <section class="col-right">
    <div class="sign-icon" style="top:404px" role="img" aria-label="Light bulb puzzle icon"></div>
    <p class="sign" style="top:398px"><strong>New trouble planning or solving problems:</strong> having a harder time paying bills or cooking recipes you have used for years.</p>
    <div class="sign-icon" style="top:503px" role="img" aria-label="Confused person icon"></div>
    <p class="sign" style="top:497px"><strong>Getting confused with time or place:</strong> forgetting where you are or how you got there, or losing track of dates or seasons.</p>
    <div class="sign-icon" style="top:597px" role="img" aria-label="Speech bubble icon"></div>
    <p class="sign" style="top:592px"><strong>Getting harder to use words when talking or writing:</strong> having trouble keeping up with or joining a conversation or struggling to find a word you are looking for (saying “that thing on your wrist that tells time” instead of “watch”).</p>
    <div class="sign-icon" style="top:725px" role="img" aria-label="Balance scale icon"></div>
    <p class="sign" style="top:719px"><strong>More slips in judgment or acting fast without thinking:</strong> more likely to be a scam victim, spending money you don't have, paying less attention to how you look, not washing up regularly, or forgetting to take care of your pet.</p>
    <div class="sign-icon" style="top:845px" role="img" aria-label="Head with leaves icon"></div>
    <p class="sign" style="top:840px"><strong>Changes in mood or personality:</strong> getting angry or sad easily in every day situations, being more fearful, suspicious, or depressed for no reason.</p>
  </section>

  <div class="partner">
    <span class="partner-square"></span>
    <span class="partner-name">CIRCLE OF ELDERS<br>AGING NETWORK</span>
  </div>
  <div class="partner-mini">
    <span class="partner-square"></span>
    <span>CIRCLE OF ELDERS AGING NETWORK</span>
  </div>

  <div class="band band--bottom"></div>
  <footer class="footer">
    <div class="footer-text">
      <p>American Indian and Alaska Native elders have a higher risk of dementia &amp; younger Indian and Native people report more memory problems at a younger age.</p>
      <p>Big changes in memory, thinking, and ability that make it hard to get through the day are not a normal part of aging.</p>
      <p>People with one or more of these 10 warning signs should see their doctor to find the cause.</p>
      <p>Other health problems may also cause these same symptoms and may be treated.<br>Early diagnosis gives you a chance to get care and plan for your future.</p>
    </div>
    <aside class="callout">
      <div class="callout-head">Early diagnosis gives you a chance to get care and plan for your future.</div>
      <div class="callout-links">www.eldermindcenter.org<br>www.healthyagingnow.org</div>
    </aside>
  </footer>
</main>
</body>
</html>
```